Professional Letterhead for electronic use

I would like to inquire, if you could help me to create a letterhead, mostly for electronic use. Preferably in word file, with fixed letterhead design (header and footer), but will allow to add text on the main body of the letter. I usually operate online and would like to be able to add text, convert it to PDF and send as an attachment.
Target Market(s)
High net worth clients.
Industry/Entity Type
Real Estate Agent
Font styles to use
Other font styles liked:
- Century Gothic
Requirements
Must have
- Company name, logo, full address, email address, landline number, website address, Homestead Adjudicator logo, PELV logo, Company registration number
Nice to have
- Professional and elegant design

```html
<!DOCTYPE html>
<html lang="en">
<head>
<meta charset="utf-8">
<title>Varenne Estate Agents – Letterhead and Folder</title>
<link href="https://fonts.googleapis.com/css2?family=Didact+Gothic&family=Questrial&display=swap" rel="stylesheet">
<style>
  :root{
    --canvas:#e6e9ea;
    --paper:#ffffff;
    --plum:#4b1a33;
    --plum-tab:#451730;
    --orange:#e8531f;
    --orange-light:#f08a4b;
    --ink:#3a3a3a;
    --badge-navy:#1f3a78;
    --badge-green:#2e8a3a;
  }
  *{margin:0;padding:0;box-sizing:border-box}
  html,body{width:1200px;height:784px;overflow:hidden}
  body{background:var(--canvas);position:relative;font-family:"Didact Gothic",sans-serif;color:var(--ink)}
  .letterhead,.folder{position:absolute;top:45px;width:513px;height:696px;border-radius:12px;overflow:hidden;box-shadow:0 2px 6px rgba(0,0,0,.18)}
  .letterhead{left:42px;background:var(--paper)}
  .folder{left:634px;background:var(--plum)}
  .swoosh{position:absolute;left:0;top:0}
  .brand-mark{position:absolute;border-radius:50%;background:radial-gradient(circle at 35% 35%,var(--orange-light),var(--orange))}
  .letterhead .brand-mark{left:243px;top:27px;width:62px;height:62px}
  .brand-name{position:absolute;font-family:"Questrial",sans-serif;letter-spacing:5px}
  .letterhead .brand-name{left:324px;top:38px;font-size:24px;color:var(--plum)}
  .brand-tag{position:absolute;font-family:"Questrial",sans-serif;color:var(--orange)}
  .letterhead .brand-tag{left:326px;top:70px;font-size:10.5px;letter-spacing:3px}
  .crn{position:absolute;left:343px;top:85px;font-size:9.5px;letter-spacing:1.5px;color:var(--plum)}
  .letter-body{position:absolute;left:66px;top:129px;width:411px;font-size:10.5px;line-height:17.5px;text-align:justify;color:var(--ink)}
  .letter-body p{margin-bottom:17.5px}
  .signature{position:absolute;left:389px;top:563px}
  .signature .name{font-size:14px;color:#333}
  .signature .role{font-size:10px;margin-top:6px;color:#333}
  .badge{position:absolute}
  .badge-adjudicator{left:51px;top:615px;width:69px;height:26px;background:var(--badge-navy)}
  .badge-pelv{left:134px;top:605px;width:52px;height:36px;border-radius:50%;background:var(--badge-green)}
  .footer-rule{position:absolute;top:654px;height:1.5px;background:var(--orange)}
  .footer-rule.left{left:0;width:180px}
  .footer-rule.right{left:353px;width:160px}
  .website{position:absolute;left:180px;width:173px;top:647px;text-align:center;font-size:11px;letter-spacing:2px;font-weight:bold;color:#333}
  .contacts{position:absolute;left:0;width:513px;top:669px;display:flex;justify-content:center;gap:10px;font-size:8.6px;color:#444;white-space:nowrap}
  .contacts span{display:flex;align-items:center;gap:3px}
  .folder-tab{position:absolute;right:0;top:150px;width:34px;height:215px;background:var(--plum-tab);border-radius:16px 0 0 16px}
  .folder .brand-mark{left:202px;top:375px;width:130px;height:130px}
  .folder .brand-name{left:0;width:513px;text-align:center;top:545px;font-size:38px;letter-spacing:10px;color:#fff}
  .folder .brand-tag{left:0;width:513px;text-align:center;top:603px;font-size:15px;letter-spacing:5px}
</style>
</head>
<body>
  <section class="letterhead">
    <svg class="swoosh" width="513" height="696" viewBox="0 0 513 696" aria-hidden="true">
      <defs>
        <linearGradient id="topBand" x1="0" y1="0" x2="1" y2="0">
          <stop offset="0" stop-color="#e8531f"/>
          <stop offset="1" stop-color="#f08a4b"/>
        </linearGradient>
      </defs>
      <path d="M0,0 H150 C60,30 30,100 30,260 C30,440 35,540 70,600 C20,540 0,440 0,330 Z" fill="url(#topBand)"/>
      <path d="M168,0 H190 C90,30 50,100 50,260 C50,440 55,540 98,604 C50,545 40,440 40,260 C40,110 80,35 168,0 Z" fill="#f08a4b"/>
    </svg>

    <div class="brand-mark" aria-hidden="true"></div>
    <div class="brand-name">VARENNE</div>
    <div class="brand-tag">ESTATE AGENTS</div>
    <div class="crn">CRN: 4172 90KD</div>

    <div class="letter-body">
      <p>Lorem ipsum dolor sit amet, consectetur adipiscing elit. Donec orci purus, luctus vitae dignissim eu, iaculis sed purus. Vivamus faucibus, ipsum nec aliquet viverra, leo mauris condimentum ligula, sit amet sagittis enim ligula quis arcu. Nam egestas tortor id nisi porttitor mattis. In tortor ante, ultricies in suscipit a, tempus non massa. Vivamus et auctor mi. Fusce vel massa nulla. Phasellus nec eros mauris, et scelerisque orci. Donec malesuada orci vitae nulla accumsan porta a id massa.</p>
      <p>Quisque accumsan iaculis magna sit amet fringilla. Maecenas consequat, magna eget tincidunt semper, odio nibh rutrum mi, id feugiat ante nisi eu risus. Vestibulum nunc orci, rhoncus a placerat in, ultricies in mi. Cras mattis varius eros, vel fringilla nisi suscipit eget. Quisque scelerisque sagittis nulla at porttitor. Mauris a justo et tellus interdum tristique. Sed id augue vitae urna euismod commodo aliquet a quam. Pellentesque arcu velit, cursus et malesuada ut, consequat et diam. Nullam erat sem, rhoncus id ullamcorper vitae, rhoncus et arcu. In ultricies ultricies nulla.</p>
      <p>Kut rutrum nisi iaculis at. Donec eu magna a metus ornare faucibus. Fusce aliquet faucibus ultricies. Morbi semper, est id tincidunt gravida, sem arcu adipiscing lacus, ac bibendum nulla leo eu purus. Quisque nec diam sed risus consectetur a ccumsan quis quis nibh. Vestibulum id purus lorem. Donec eu magna a metus ornare faucibus. Fusce aliquet faucibus ultricies. Morbi semper, est id tincidunt gravida, sem arcu adipiscing lacus, ac bibendum nulla leo eu purus. Quisque nec diam sed risus consectetur a ccumsan quis quis nibh. Vestibulum id purus lorem.</p>
    </div>

    <div class="signature">
      <div class="name">Elliot Marsh</div>
      <div class="role">Co-Founder &amp; CEO</div>
    </div>

    <div class="badge badge-adjudicator" role="img" aria-label="Homestead Adjudicator membership badge"></div>
    <div class="badge badge-pelv" role="img" aria-label="PELV membership badge"></div>

    <div class="footer-rule left"></div>
    <div class="website">www.varenneestate.org</div>
    <div class="footer-rule right"></div>

    <div class="contacts">
      <span>
        <svg width="10" height="9" viewBox="0 0 10 9" aria-hidden="true"><path d="M1,3 Q5,0 9,3 L8,4 L6,3.5 L6,2.5 Q5,2.2 4,2.5 L4,3.5 L2,4 Z M2,5 H8 L9,8.5 H1 Z" fill="#e8531f"/></svg>
        (555) 214-3080
      </span>
      <span>
        <svg width="10" height="9" viewBox="0 0 10 9" aria-hidden="true"><rect x="2.5" y="0.5" width="5" height="3" fill="#e8531f"/><rect x="0.5" y="3.5" width="9" height="3.5" rx="1" fill="#e8531f"/><rect x="2.5" y="6" width="5" height="2.5" fill="#e8531f"/></svg>
        (555) 214-3081
      </span>
      <span>
        <svg width="11" height="8" viewBox="0 0 11 8" aria-hidden="true"><rect x="0.5" y="0.5" width="10" height="7" fill="#e8531f"/><path d="M0.5,0.5 L5.5,4.5 L10.5,0.5" fill="none" stroke="#fff" stroke-width="1"/></svg>
        hello@varenneestate.org
      </span>
      <span>
        <svg width="8" height="10" viewBox="0 0 8 10" aria-hidden="true"><path d="M4,0 A4,4 0 0 1 8,4 C8,6.5 4,10 4,10 C4,10 0,6.5 0,4 A4,4 0 0 1 4,0 Z" fill="#e8531f"/><circle cx="4" cy="4" r="1.5" fill="#fff"/></svg>
        410 Alder Crest Lane, Fairhaven, MI 48000
      </span>
    </div>
  </section>

  <section class="folder">
    <div class="folder-tab" aria-hidden="true"></div>
    <div class="brand-mark" aria-hidden="true"></div>
    <div class="brand-name">VARENNE</div>
    <div class="brand-tag">ESTATE AGENTS</div>
  </section>
</body>
</html>
```